Attractive door board for entrance beautysalon

Make an attractive design for a board that can be glued on the front door of a beauty salon. The salon location has no window in the front so I need something catchy and attractive. The door board contains a list of the services and the website: www.velmora.be, and the text "Enkel op afspraak, bel 0486319542"

Target Market(s)

woman between 16 and 99 years old

Industry/Entity Type

Beauty Salon

Font styles to use
Sans Serif

Requirements
Must have
• A very nice, attractive but sober design.
• It must have a classy Marvaux, Quen, ... chique design.
• The logo must be on it (in attachment)
• There must be the following list in it:
• Gelaatsverzorging
• Wimperverlenging
• Wimperlifting
• Suikerontharing
• Permanente Make Up
• Airbrush Tanning
• Manicure - Pedicure - Tovira
• and then the website www.velmora.be, and the text "Enkel op afspraak, bel 0486319542"
Nice to have
• a catchy design,
• max. width can be 75 cm and max height 180 cm as it is a design for a board that will be glued on a door.
Should not have
• orchid flowers, buddha look a likes

```html
<!DOCTYPE html>
<html lang="nl">
<head>
<meta charset="utf-8">
<title>Velmora – Schoonheidsinstituut</title>
<link rel="stylesheet" href="https://fonts.googleapis.com/css2?family=Josefin+Sans:wght@300;400&family=Crimson+Pro:wght@400&family=Cousine&family=Open+Sans:wght@600&display=swap">
<style>
  :root{
    --ink:#000;
    --paper:#fff;
    --blush:#f3a99b;
    --rose-gold:#e7b3a4;
    --frame:#6e6e6e;
    --band:#3a3a3a;
  }
  *{margin:0;padding:0;box-sizing:border-box}
  html,body{width:1200px;height:2890px;overflow:hidden;background:var(--ink)}
  .board{position:relative;width:1200px;height:2890px;background:var(--ink);overflow:hidden}

  .hero{position:absolute;left:0;top:0;width:1200px;height:830px;
    background:
      radial-gradient(ellipse 38% 30% at 50% 88%, #6b3a3e 0%, rgba(107,58,62,0) 100%),
      radial-gradient(ellipse 30% 40% at 18% 35%, #4a3d3a 0%, rgba(74,61,58,0) 100%),
      radial-gradient(ellipse 30% 40% at 82% 35%, #4a3d3a 0%, rgba(74,61,58,0) 100%),
      radial-gradient(ellipse at 50% 45%, #5a4a48 0%, #2e2626 60%, #1a1515 100%)}
  .brand-mark{position:absolute;left:450px;top:70px;width:300px;height:300px}
  .brand-name{position:absolute;left:0;width:1200px;top:498px;text-align:center;line-height:1;
    font-family:"Josefin Sans",sans-serif;font-weight:300;font-size:86px;letter-spacing:0.55em;
    padding-left:0.55em;color:var(--paper)}
  .brand-tag{position:absolute;left:28px;top:606px;width:1112px;height:112px;
    border:2px solid #b9b0b0;display:flex;align-items:center;justify-content:center;
    font-family:"Josefin Sans",sans-serif;font-weight:400;font-size:25px;letter-spacing:0.72em;
    padding-left:0.72em;color:var(--rose-gold)}

  .collage{position:absolute;left:36px;top:774px;width:1104px;height:956px;background:var(--paper)}
  .tile{position:absolute}
  .laser-card{position:absolute;left:4px;top:678px;width:361px;height:273px;background:var(--paper);
    display:flex;flex-direction:column;justify-content:flex-end;align-items:flex-start;
    padding:0 0 26px 6px;font-family:"Josefin Sans",sans-serif;color:#111;white-space:nowrap}
  .laser-card .name{font-size:32px;font-weight:400;letter-spacing:0.1em;line-height:1}
  .laser-card .sub{font-size:21px;font-weight:400;letter-spacing:0.06em;margin-top:10px;line-height:1}

  .services{position:absolute;left:40px;top:1832px;width:1088px;height:566px;border:2px solid var(--frame)}
  .service-list{position:absolute;left:84px;top:1786px;list-style:none;
    font-family:"Crimson Pro",serif;font-size:73px;line-height:90.5px;color:var(--blush);white-space:nowrap}
  .service-list li span{background:var(--ink);padding-right:8px}

  .footer{position:absolute;left:0;top:2496px;width:1200px;height:394px;
    background:
      radial-gradient(ellipse 22% 40% at 74% 55%, #6a5a54 0%, rgba(106,90,84,0) 100%),
      linear-gradient(180deg,#2a2a2a 0%,#4a4646 45%,#3c3838 100%)}
  .website{position:absolute;left:0;top:2668px;width:1200px;text-align:center;line-height:1;
    font-family:"Cousine",monospace;font-size:104px;letter-spacing:0.04em;color:var(--paper)}
  .appointment{position:absolute;left:0;top:2762px;width:1200px;height:92px;background:var(--band);
    display:flex;align-items:center;justify-content:center;
    font-family:"Open Sans",sans-serif;font-weight:600;font-size:48px;color:var(--paper)}
</style>
</head>
<body>
<main class="board">
  <section class="hero" role="img" aria-label="Portret van een vrouw met gelakte nagels, handen over de ogen"></section>
  <svg class="brand-mark" viewBox="0 0 300 300" aria-hidden="true">
    <circle cx="150" cy="150" r="140" fill="none" stroke="#e7b3a4" stroke-width="4"/>
  </svg>
  <h1 class="brand-name">VELMORA</h1>
  <p class="brand-tag">SCHOONHEIDSINSTITUUT</p>

  <section class="collage">
    <div class="tile" style="left:4px;top:4px;width:546px;height:389px;background:linear-gradient(180deg,#e9c7b3 0%,#d9ab93 30%,#f2ddd2 50%,#e3bba5 70%,#cf9c84 100%)" role="img" aria-label="Gesloten ogen met natuurlijke en verlengde wimpers"></div>
    <div class="tile" style="left:554px;top:4px;width:183px;height:257px;background:linear-gradient(180deg,#d8d4cc 0%,#c9c3ba 40%,#f0c4c6 62%,#cfe6bf 100%)" role="img" aria-label="Wimperserum en verzorgende lotions"></div>
    <div class="tile" style="left:741px;top:4px;width:359px;height:257px;background:linear-gradient(180deg,#f4f1ee 0%,#e2ddd6 45%,#bdb3a8 75%,#8f8479 100%)" role="img" aria-label="Interieur van het salon met productrekken"></div>
    <div class="tile" style="left:554px;top:265px;width:361px;height:269px;background:linear-gradient(135deg,#e6e6e6 0%,#cfcfcf 45%,#6b6b4e 70%,#c7c39a 100%)" role="img" aria-label="Materiaal voor wimperverlenging met pincetten"></div>
    <div class="tile" style="left:919px;top:265px;width:181px;height:269px;background:linear-gradient(180deg,#f7f7f7 0%,#cfe9e2 55%,#a8d6c9 100%)" role="img" aria-label="Potjes gezichtscrème"></div>
    <div class="tile" style="left:4px;top:418px;width:181px;height:249px;background:linear-gradient(180deg,#f0f0f0 0%,#9a9a9a 55%,#d9d9d9 100%)" role="img" aria-label="Laserbehandeling voor ontharing"></div>
    <div class="tile" style="left:189px;top:401px;width:176px;height:269px;background:linear-gradient(180deg,#f1e6df 0%,#d4a58c 40%,#e2bca6 100%)" role="img" aria-label="Vrouw met verzorgde huid"></div>
    <div class="tile" style="left:369px;top:401px;width:181px;height:137px;background:linear-gradient(180deg,#fbfbfb 0%,#e4e4e4 60%,#b3aca2 100%)" role="img" aria-label="Huidverzorgingsproducten"></div>
    <div class="tile" style="left:369px;top:542px;width:181px;height:128px;background:linear-gradient(135deg,#e9985f 0%,#f2efe9 55%,#c7714a 100%)" role="img" aria-label="Wimpers worden aangebracht met pincet"></div>
    <div class="tile" style="left:554px;top:538px;width:181px;height:273px;background:linear-gradient(180deg,#b9987e 0%,#d6b49c 40%,#8aa4b0 60%,#c59f85 100%)" role="img" aria-label="Permanente make-up van wenkbrauw en oog"></div>
    <div class="tile" style="left:739px;top:554px;width:176px;height:237px;background:linear-gradient(135deg,#6f6f6f 0%,#d8d8d8 45%,#9a9a9a 100%)" role="img" aria-label="Gladde benen na ontharing"></div>
    <div class="tile" style="left:919px;top:554px;width:181px;height:241px;background:linear-gradient(180deg,#f4f4f4 0%,#9c9c9c 40%,#e7e7e7 60%,#4a4a4a 100%)" role="img" aria-label="Vrouw in zomerjurk"></div>
    <div class="laser-card">
      <span class="name">ARDELLE LASER</span>
      <span class="sub">permanente ontharing</span>
    </div>
    <div class="tile" style="left:369px;top:674px;width:181px;height:137px;background:linear-gradient(180deg,#f1ead9 0%,#e0b791 50%,#c98d68 100%)" role="img" aria-label="Gezichtsverzorging"></div>
    <div class="tile" style="left:369px;top:815px;width:181px;height:132px;background:linear-gradient(180deg,#f3ede9 0%,#ddb8a2 55%,#f0e6df 100%)" role="img" aria-label="Stralende huid"></div>
    <div class="tile" style="left:554px;top:815px;width:181px;height:136px;background:linear-gradient(90deg,#fbfbfb 0%,#e7d5c8 35%,#a9704e 70%,#f4ece6 100%)" role="img" aria-label="Reiniging van het gezicht"></div>
    <div class="tile" style="left:739px;top:815px;width:160px;height:136px;background:linear-gradient(135deg,#d08a68 0%,#b4694a 50%,#8e4d36 100%)" role="img" aria-label="Gebruinde huid na airbrush tanning"></div>
  </section>

  <div class="services"></div>
  <ul class="service-list">
    <li><span>Gelaatsverzorging</span></li>
    <li>Wimperverlenging</li>
    <li>Wimperlifting</li>
    <li>Suikerontharing</li>
    <li>Permanente Make Up</li>
    <li>Airbrush Tanning</li>
    <li><span>Manicure - Pedicure - Tovira</span></li>
  </ul>

  <section class="footer" role="img" aria-label="Vrouw in een sfeervol interieur"></section>
  <p class="website">www.velmora.be</p>
  <p class="appointment">Enkel op afspraak, Bel 0486319542</p>
</main>
</body>
</html>
```